Sweet website for Wrenfield Flowers

Our name is Wrenfield and we are looking for someone to design a SWEET looking website for us. We would like a site that has a responsive design, clean interface, easy to navigate and smooth user experience. It will be hosted on wordpress and is an ecommerce site so it needs to be fully compatible so that updates can be made easily on the back end.

It is important to us that the design is premium looking, beautiful to look at and has an elegance to it that befits the beautiful products we sell. We don't want it to look like a standard wordpress template so please feel free to be creative.

We have defined basic template pages in wireframes which are NOT by any means a design mandate. Please use this as a guide for what content should be considered in the design on each page. THERE ARE TWO HOMEPAGE OPTIONS (1 has additional content areas - please propose designs for both options) We DO NOT want to see creative that looks exactly like our wireframes. Please come up with fresh creative ideas. (see wireframe doc attached). We have also attached the copy deck, logos, design references to help you to better understand what our customers like.

THANK YOU! LOOKING FORWARD TO SEEING YOUR PROPOSALS!!!
Updates

An updated content/wireframe document has been uploaded. We have 2 content options for the homepage - please propose designs for both layouts.

We have also added a powerpoint with websites that we like so that you can get a better idea of what we would like our website to look like.

Project Deadline Extended
Reason: We are extending the deadline and have increased and guaranteed the payment since we can see potential in the submitted designs but feel that they are currently not at their creative potential. The extra time given should allow for more time to submit original designs that do not look exactly like the wireframes provided.

Target Market(s)

Premium, affluent market

Font styles to use
Sans Serif

Requirements
Must have
• see wireframe, copy and design reference attachments and use as guidelines. The powerpoint presentation shows key areas that we think will be good in our design. Please review them. There are 2 homepage content options. Please propose options for both.
Please take note that option 2 has 3 additional content areas labelled "hand tied bouquets shop now", "Hatbox arrangements shop now" "floral cupcakes shop now" please propose 1 design with this the additional sections and 1 design without.

```html
<!DOCTYPE html>
<html lang="en">
<head>
<meta charset="utf-8">
<title>Wrenfield Flowers</title>
<link href="https://fonts.googleapis.com/css2?family=Arimo:wght@400;700&family=Kaushan+Script&display=swap" rel="stylesheet">
<style>
:root{
  --plum:#5b1f45;
  --plum-dark:#4a1637;
  --pink:#d9478a;
  --pink-light:#ee7fb2;
  --pink-soft:#fbe6ef;
  --rose-title:#c2306f;
  --text:#3c1530;
  --white:#fff;
  --footer:#2f2f2f;
  --footer-line:#454545;
  --footer-text:#cfcfcf;
}
*{box-sizing:border-box;margin:0;padding:0}
html,body{width:998px;height:1200px;overflow:hidden}
body{position:relative;background:radial-gradient(ellipse at 50% 30%,#67264f 0%,var(--plum) 55%,var(--plum-dark) 100%);font-family:"Arimo",Arial,sans-serif;color:var(--text)}
.abs{position:absolute}
/* header */
.brand{left:130px;top:10px;width:130px;text-align:center;color:var(--pink-light)}
.brand-dot{display:block;margin:0 auto 4px;width:22px;height:22px;border-radius:50%;background:var(--pink)}
.brand-name{font-size:19px;letter-spacing:3px;line-height:1}
.brand-sub{font-size:10px;letter-spacing:3px;margin-top:2px}
.search{left:410px;top:49px;width:180px;height:24px;border-radius:4px;background:#d9c4cf;border:1px solid #8c5a77;display:flex}
.search span{flex:1;font-size:11px;color:#7d6070;padding:5px 7px}
.search i{width:26px;border-left:1px solid #9c7a8c;display:flex;align-items:center;justify-content:center}
.account{top:24px;font-size:10.5px;color:#f1c4da;display:flex;align-items:center;gap:6px;text-decoration:underline;white-space:nowrap}
.account b{width:20px;height:20px;border-radius:50%;background:#3b0f2b;display:flex;align-items:center;justify-content:center}
.nav{left:130px;top:79px;width:740px;height:31px;border-radius:3px;background:linear-gradient(#ee7db0,#cf4686);display:flex;box-shadow:0 2px 3px rgba(0,0,0,.3);overflow:hidden}
.nav a{flex:none;display:flex;align-items:center;justify-content:center;height:31px;color:var(--white);font-size:11px;text-decoration:none;white-space:nowrap;border-right:1px solid rgba(255,255,255,.3)}
/* slider */
.hero{left:130px;top:132px;width:546px;height:245px;background:radial-gradient(circle at 55% 45%,#e79bd6 0%,#f2a7bd 40%,#f1b1ae 65%,#6d8a4d 100%)}
.ribbon{left:130px;top:132px}
.side{left:676px;top:132px;width:194px;height:245px;background:var(--pink-soft)}
.side-item{height:61px;border-bottom:1px solid #e8b8cc;display:flex;gap:8px;padding:7px 8px}
.side-thumb{width:56px;height:44px;flex:none;border:2px solid var(--white)}
.side-item h4{font-size:9px;color:var(--pink);text-transform:uppercase;font-weight:700}
.side-item p{font-size:9px;color:#555;line-height:12px;margin-top:2px}
/* main panel */
.panel{left:130px;top:400px;width:740px;height:536px;background:var(--white);border-top:7px solid var(--pink-light);box-shadow:0 2px 8px rgba(0,0,0,.4)}
.product{position:absolute;top:17px;width:180px;height:196px;padding:0 12px;border-right:1px solid #e6e6e6}
.product h3{font-size:12.5px;color:var(--pink);font-weight:700}
.product .price{font-size:11px;color:#333;font-weight:700;margin-top:4px}
.product .pic{width:90px;height:100px;margin:18px auto 0}
.product .cart{position:absolute;left:12px;top:168px;width:74px;height:25px;border-radius:3px;background:linear-gradient(#555,#1d1d1d);color:var(--white);font-size:10.5px;text-align:center;line-height:25px;white-space:nowrap}
.product .more{position:absolute;left:110px;top:172px;font-size:10px;color:#c27a9d;border-bottom:1px dotted #c27a9d;white-space:nowrap}
.next{left:720px;top:100px;width:20px;height:22px;background:#d0d0d0}
.divider{left:11px;top:228px;width:718px;border-top:1px dashed #ccc}
.feature{position:absolute;top:258px;width:220px}
.feature h2{font-family:"Kaushan Script",cursive;font-size:24px;font-weight:400;color:var(--rose-title);line-height:1;white-space:nowrap}
.feature .pic{margin-top:12px;height:96px;border:4px solid var(--white);outline:1px solid #ddd}
.feature p{margin-top:18px;font-size:10.5px;line-height:14.5px;color:var(--text)}
/* footer */
.footer{left:0;top:991px;width:998px;height:209px;background:var(--footer);border-top:1px solid #1e1e1e}
.top-btn{left:833px;top:973px;width:36px;height:36px;border-radius:50%;background:#bdbdbd;border:2px solid #e4e4e4;color:#333;font-size:8px;font-weight:700;text-align:center;line-height:32px}
.f-col{top:1013px;color:var(--footer-text);font-size:10.5px;line-height:16px}
.f-col h5{color:var(--pink-light);font-size:11.5px;margin-bottom:16px}
.signup{display:flex;gap:8px;margin-top:18px}
.signup span{width:154px;height:22px;background:#474747;border:1px solid #555;font-size:10px;color:#999;padding:3px 4px}
.signup b{width:46px;height:24px;background:linear-gradient(#5a5a5a,#3a3a3a);color:#ddd;font-weight:400;text-align:center;line-height:24px;border-radius:2px}
.socials{display:flex;gap:9px;margin-top:16px}
.socials i{width:19px;height:19px;border-radius:3px;background:#6b8bb8}
.links a{display:block;color:var(--footer-text);text-decoration:none;border-bottom:1px solid var(--footer-line);padding:4px 0 6px 10px;margin-bottom:6px;width:246px;position:relative}
.links a::before{content:"";position:absolute;left:0;top:8px;border:3px solid transparent;border-left-color:#aaa}
.copy{left:0;top:1158px;width:998px;text-align:center;font-size:9px;color:#ccc}
</style>
</head>
<body>
<header>
  <div class="abs brand"><span class="brand-dot"></span><div class="brand-name">WRENFIELD</div><div class="brand-sub">FLOWERS</div></div>
  <div class="abs search"><span>Search...</span><i><svg width="12" height="12" viewBox="0 0 12 12"><circle cx="5" cy="5" r="3.5" fill="none" stroke="#5a3a4d" stroke-width="1.5"/><line x1="7.5" y1="7.5" x2="11" y2="11" stroke="#5a3a4d" stroke-width="1.8"/></svg></i></div>
  <div class="abs account" style="left:712px"><b><svg width="10" height="10" viewBox="0 0 10 10"><circle cx="3" cy="3" r="2" fill="none" stroke="#f1c4da"/><line x1="4.5" y1="4.5" x2="9" y2="9" stroke="#f1c4da" stroke-width="1.4"/></svg></b>My Account</div>
  <div class="abs account" style="left:800px"><svg width="14" height="12" viewBox="0 0 14 12"><path d="M0 1h3l2 7h7l2-5H4" fill="none" stroke="#f1c4da" stroke-width="1.4"/><circle cx="6" cy="10.5" r="1.2" fill="#f1c4da"/><circle cx="11" cy="10.5" r="1.2" fill="#f1c4da"/></svg>My Cart ( 0 )</div>
  <nav class="abs nav">
    <a href="#" style="width:38px"><svg width="12" height="11" viewBox="0 0 12 11"><path d="M6 0L0 5h2v6h3V7h2v4h3V5h2z" fill="#fff"/></svg></a>
    <a href="#" style="width:86px">Buy Flowers</a>
    <a href="#" style="width:115px">Season's Collection</a>
    <a href="#" style="width:126px">Weddings &amp; Contracts</a>
    <a href="#" style="width:115px">Gifts &amp; Accessories</a>
    <a href="#" style="width:67px">Updates</a>
    <a href="#" style="width:43px">Blog</a>
    <a href="#" style="width:48px">FAQ</a>
    <a href="#" style="width:71px;border:none">Contact</a>
  </nav>
</header>

<section>
  <div class="abs hero" role="img" aria-label="Featured photo of pink roses arranged in a ring"></div>
  <svg class="abs ribbon" width="62" height="62" viewBox="0 0 62 62"><path d="M0 36L36 0h22L0 58z" fill="#c4183c"/><text x="14" y="40" transform="rotate(-45 14 40)" font-family="Arimo,Arial,sans-serif" font-size="8" fill="#fff">FEATURED</text></svg>
  <div class="abs side">
    <div class="side-item"><div class="side-thumb" role="img" aria-label="Pink roses thumbnail" style="background:#f09ad0"></div><div><h4>Pink Roses</h4><p>Lorem Ipsum is simply dummy text of the printing.</p></div></div>
    <div class="side-item"><div class="side-thumb" role="img" aria-label="Yellow flowers thumbnail" style="background:#e8c45a"></div><div><h4>Sunny Yellow</h4><p>Lorem Ipsum is simply dummy text of the printing.</p></div></div>
    <div class="side-item"><div class="side-thumb" role="img" aria-label="Tulips thumbnail" style="background:#e8b0c2"></div><div><h4>All Tulips</h4><p>Lorem Ipsum is simply dummy text of the printing.</p></div></div>
    <div class="side-item" style="border:none"><div class="side-thumb" role="img" aria-label="Orange flowers thumbnail" style="background:#ef8a5a"></div><div><h4>Sunny Deals</h4><p>Lorem Ipsum is simply dummy text of the printing.</p></div></div>
  </div>
</section>

<main class="abs panel">
  <div class="product" style="left:10px"><h3>Amazonia</h3><div class="price">$39.99</div><div class="pic" role="img" aria-label="Tropical orange bouquet" style="background:radial-gradient(#e8733a,#fff 72%)"></div><span class="cart">Add to cart</span><span class="more">View more...</span></div>
  <div class="product" style="left:190px"><h3>Reflection</h3><div class="price">$13</div><div class="pic" role="img" aria-label="Red and white rose bouquet" style="background:radial-gradient(#d9526a,#fff 72%)"></div><span class="cart">Add to cart</span><span class="more">View more...</span></div>
  <div class="product" style="left:370px"><h3>Peace</h3><div class="price">$30.99</div><div class="pic" role="img" aria-label="White lily bouquet" style="background:radial-gradient(#dfe3c8,#fff 72%)"></div><span class="cart">Add to cart</span><span class="more">View more...</span></div>
  <div class="product" style="left:550px;border:none"><h3>Twilight</h3><div class="price">Free!</div><div class="pic" role="img" aria-label="Lilac and white bouquet in a vase" style="background:radial-gradient(#b9a0d4,#fff 72%)"></div><span class="cart">Add to cart</span><span class="more">View more...</span></div>
  <div class="abs next"><svg width="20" height="22" viewBox="0 0 20 22"><path d="M8 6l5 5-5 5" fill="none" stroke="#fff" stroke-width="2"/></svg></div>
  <div class="abs divider"></div>
  <div class="feature" style="left:10px"><h2>Customer Favourites</h2><div class="pic" role="img" aria-label="Purple flowers with a gift ribbon" style="background:linear-gradient(90deg,#b33ca8,#d98ad8)"></div><p>Lorem ipsum dolor sit amet, consectetur adipiscing elit. Maecenas id rutrum orci. Donec vel turpis orci, id conditum est. Nunc nec felis non est dictum ultrices. Nam semper gravida auctor. Aenean non dolor at lorem viverra fringilla varius vitae nisi. Nunc porta turpis vitae tellus pulvinar dapibus.</p></div>
  <div class="feature" style="left:259px"><h2>Bespoke</h2><div class="pic" role="img" aria-label="Close-up of a pink lotus flower" style="background:linear-gradient(90deg,#5f8f86,#e48fb2 40%,#f2b2c8)"></div><p>Lorem ipsum dolor sit amet, consectetur adipiscing elit. Maecenas id rutrum orci. Donec vel turpis orci, id conditum est. Nunc nec felis non est dictum ultrices. Nam semper gravida auctor. Aenean non dolor at lorem viverra fringilla varius vitae nisi. Nunc porta turpis vitae tellus pulvinar dapibus.</p></div>
  <div class="feature" style="left:508px"><h2>Service Guarantee</h2><div class="pic" role="img" aria-label="Orange and white flower arrangement" style="background:linear-gradient(90deg,#e0642c,#f4e6d4 50%,#e8722e)"></div><p>Lorem ipsum dolor sit amet, consectetur adipiscing elit. Maecenas id rutrum orci. Donec vel turpis orci, id conditum est. Nunc nec felis non est dictum ultrices. Nam semper gravida auctor. Aenean non dolor at lorem viverra fringilla varius vitae nisi. Nunc porta turpis vitae tellus pulvinar dapibus.</p></div>
</main>

<footer>
  <div class="abs footer"></div>
  <div class="abs top-btn">TOP</div>
  <div class="abs f-col" style="left:130px;width:240px"><h5>Can you keep a secret?</h5><p>Join the Willow Society and get exclusive member only sale and delivery discounts when you sign up for the Willow newsletter!</p><div class="signup"><span>Enter your e-mail...</span><b>Go</b></div></div>
  <div class="abs f-col" style="left:394px;width:200px"><h5>Contact Info</h5><p>Phone : +97 155 0148 320</p><p>Email: info@wrenfieldflowers.com</p><div class="socials"><i></i><i style="background:#4fa3c9"></i><i style="background:#c43a3a"></i><i style="background:#5b9a4a"></i><i style="background:#4aa8de"></i></div></div>
  <div class="abs f-col links" style="left:624px;top:1010px"><a href="#">FAQ's</a><a href="#">Secure Payment</a><a href="#">Delivery Policy</a><a href="#">Terms &amp; Conditions</a></div>
  <div class="abs copy">Copyright © 2013, Wrenfield Flowers, All rights reserved.</div>
</footer>
</body>
</html>
```